We need a business card design for a new soccer program based in Melbourne, Victoria, Australia.
Coaching kids from 2 through to 14 develop social, motor and soccer skills, in a fun and friendly non-competitive environment.
Our company colours are blue and orange as seen in the logo attached below. However, we are happy for the font to be any modern colour that looks professional.
Target Market(s)
Mums and dads
Industry/Entity Type
Business
Contact Information for Business Card
business name: Bright Kick Soccer
Marco Delvani Director- 0491 375 618
Luke Fernholt Director- 0417 583 106
Tomas Wendhaus Head Coach
email: marco@brightkicksoccer.com.au
website: www.brightkicksoccer.com.au
Coaching kids from 2-14
https://www.facebook.com/brightkicksoccer (facebook page not required unless it looks good without being clustered)
Look and feel

```html
<!DOCTYPE html>
<html lang="en">
<head>
<meta charset="utf-8">
<title>Bright Kick Soccer – Business Card</title>
<link href="https://fonts.googleapis.com/css2?family=Open+Sans:wght@400;600;700;800&display=swap" rel="stylesheet">
<style>
  :root{
    --bg:#ecebe8;
    --orange-light:#fbbd3a;
    --orange:#f5a623;
    --orange-deep:#ee8f1c;
    --blue:#3b3fb8;
    --blue-deep:#2a2d96;
    --blue-light:#4f55d0;
    --ink:#2b2b2b;
    --white:#ffffff;
  }
  *{box-sizing:border-box;margin:0;padding:0}
  html,body{width:1200px;height:1023px;overflow:hidden}
  body{background:var(--bg);font-family:"Open Sans",Arial,sans-serif;position:relative}

  .card{position:absolute;width:540px;height:330px;border-radius:4px;overflow:hidden;
        box-shadow:0 10px 28px rgba(0,0,0,.18)}
  .card--front{left:40px;top:346px;background:linear-gradient(135deg,var(--orange-light),var(--orange) 55%,var(--orange-deep))}
  .card--back{left:620px;top:346px;background:radial-gradient(circle at 50% 50%,var(--blue-light) 0%,var(--blue) 55%,var(--blue-deep) 100%)}

  /* front */
  .brand{position:absolute;left:28px;top:0;width:190px;height:268px;display:flex;align-items:center;gap:10px}
  .brand__dot{width:26px;height:26px;border-radius:50%;background:var(--blue);flex:none}
  .brand__name{font-weight:800;font-size:26px;line-height:1.05;color:var(--blue);text-transform:uppercase}
  .divider{position:absolute;left:232px;top:30px;width:1px;height:208px;background:var(--ink);opacity:.55}

  .contacts{position:absolute;left:252px;top:26px;right:18px;color:var(--ink)}
  .person{margin-bottom:6px}
  .person__name{font-weight:600;font-size:17px;color:var(--blue);text-transform:uppercase;letter-spacing:.3px;line-height:1.15}
  .person__role{font-size:11.5px;display:flex;align-items:center;gap:5px;line-height:1.3}
  .person--small .person__name{font-size:12px;font-weight:700;color:var(--ink);text-transform:none}
  .links{margin:8px 0 8px}
  .link{font-size:11.5px;display:flex;align-items:center;gap:6px;line-height:1.45}
  .icon{width:10px;height:10px;flex:none}

  .tagline-band{position:absolute;left:0;right:0;bottom:0;height:62px;background:var(--blue);
                border-top:3px solid var(--blue-deep);display:flex;align-items:center;padding-left:28px}
  .tagline{color:var(--white);font-weight:700;font-size:22px}

  /* back */
  .back-brand{position:absolute;inset:0;display:flex;align-items:center;justify-content:center;gap:14px}
  .back-brand__dot{width:40px;height:40px;border-radius:50%;background:var(--orange)}
  .back-brand__name{font-weight:800;font-size:36px;line-height:1.02;color:var(--orange);text-transform:uppercase}
</style>
</head>
<body>

<section class="card card--front" aria-label="Business card front">
  <div class="brand">
    <span class="brand__dot"></span>
    <span class="brand__name">Bright Kick Soccer</span>
  </div>
  <div class="divider"></div>

  <div class="contacts">
    <div class="person">
      <div class="person__name">Marco Delvani</div>
      <div class="person__role">Director |
        <svg class="icon" viewBox="0 0 10 10"><rect width="10" height="10" rx="2" fill="var(--blue)"/><rect x="3" y="2" width="4" height="6" rx="1" fill="#fff"/></svg>
        0491 375 618</div>
    </div>
    <div class="person">
      <div class="person__name">Luke Fernholt</div>
      <div class="person__role">Director |
        <svg class="icon" viewBox="0 0 10 10"><rect width="10" height="10" rx="2" fill="var(--blue)"/><rect x="3" y="2" width="4" height="6" rx="1" fill="#fff"/></svg>
        0417 583 106</div>
    </div>
    <div class="person">
      <div class="person__name">Tomas Wendhaus</div>
      <div class="person__role">Head coach</div>
    </div>

    <div class="links">
      <div class="link">
        <svg class="icon" viewBox="0 0 10 10"><rect width="10" height="10" rx="2" fill="var(--blue)"/><path d="M2 3h6v4H2z M2 3l3 2.2L8 3" fill="none" stroke="#fff" stroke-width="0.9"/></svg>
        marco@brightkicksoccer.com.au</div>
      <div class="link">
        <svg class="icon" viewBox="0 0 10 10"><rect width="10" height="10" rx="2" fill="var(--blue)"/><circle cx="5" cy="5" r="2.8" fill="none" stroke="#fff" stroke-width="0.9"/></svg>
        www.brightkicksoccer.com.au</div>
      <div class="link">
        <svg class="icon" viewBox="0 0 10 10"><rect width="10" height="10" rx="2" fill="var(--blue)"/></svg>
        /brightkicksoccer</div>
    </div>

    <div class="person person--small">
      <div class="person__name">Daniel Orsetti</div>
      <div class="person__role">Coach |
        <svg class="icon" viewBox="0 0 10 10"><rect width="10" height="10" rx="2" fill="var(--blue)"/><rect x="3" y="2" width="4" height="6" rx="1" fill="#fff"/></svg>
        0452 180 934</div>
    </div>
  </div>

  <div class="tagline-band"><span class="tagline">Coaching kids from 2-14</span></div>
</section>

<section class="card card--back" aria-label="Business card back">
  <div class="back-brand">
    <span class="back-brand__dot"></span>
    <span class="back-brand__name">Bright<br>Kick<br>Soccer</span>
  </div>
</section>

</body>
</html>
```